Business card

We are looking for a creative person to deigns our company business card.

Target Market(s)

College age student

Industry/Entity Type

Accommodation

Contact Information for Business Card

We want a fun, clean and sophisticated design. It should look good, but more importantly the information should be legible.

Font styles to use
Serif
Sans Serif
Other font styles liked:
• Open Sans ,

Colors
33a6d7

Requirements
Must have
• Must have a young and memorable message. Be legible.
• Our logo on the back on a solid blue , please find color and logo attached
• LodgeBridgely.net on the back.
Nice to have
• I would like to have couple of different fonts on the LodgeBridgely.net on the back of the cards with a solid blue.

```html
<!DOCTYPE html>
<html lang="en">
<head>
<meta charset="utf-8">
<title>LodgeBridgely Business Card</title>
<link rel="stylesheet" href="https://fonts.googleapis.com/css2?family=Roboto:wght@400;500;700&display=swap">
<style>
  :root {
    --page-bg: #ece9e4;
    --navy: #034a7b;
    --brand-blue: #3a9ad9;
    --brand-blue-deep: #2f8fd2;
    --back-blue: #3f9ee0;
    --ink-navy: #0a4a7c;
    --white: #ffffff;
    --faint: rgba(255, 255, 255, 0.14);
  }
  * { box-sizing: border-box; margin: 0; padding: 0; }
  html, body {
    width: 1200px;
    height: 545px;
    overflow: hidden;
  }
  body {
    background: var(--page-bg);
    font-family: "Roboto", sans-serif;
    color: var(--white);
    position: relative;
  }
  .card {
    position: absolute;
    top: 118px;
    height: 300px;
    border-radius: 22px;
    overflow: hidden;
  }
  /* Front */
  .card-front {
    left: 67px;
    width: 518px;
    background: linear-gradient(180deg, var(--brand-blue) 0%, var(--brand-blue-deep) 100%);
  }
  .front-header {
    position: absolute;
    left: 0; top: 0;
    width: 100%;
    height: 104px;
    background: var(--navy);
    border-bottom: 3px solid var(--white);
  }
  .holder-name {
    position: absolute;
    left: 36px; top: 33px;
    font-size: 25px;
    font-weight: 700;
    letter-spacing: 0.3px;
  }
  .holder-title {
    position: absolute;
    left: 37px; top: 62px;
    font-size: 13.5px;
    font-weight: 500;
    letter-spacing: 0.3px;
  }
  .brand-circle {
    position: absolute;
    left: 234px; top: 15px;
    width: 266px; height: 266px;
    border-radius: 50%;
    background: var(--white);
    display: flex;
    align-items: center;
    justify-content: center;
  }
  .brand-circle .brand-name {
    font-size: 27px;
    font-weight: 700;
    color: var(--ink-navy);
    letter-spacing: -0.3px;
  }
  .address {
    position: absolute;
    left: 36px; top: 153px;
    font-size: 14px;
    line-height: 19px;
  }
  .contact-list {
    position: absolute;
    left: 36px; top: 199px;
    list-style: none;
    font-size: 13.5px;
  }
  .contact-list li {
    display: flex;
    align-items: center;
    height: 20px;
  }
  .contact-icon {
    width: 15px; height: 15px;
    margin-right: 11px;
    flex: none;
  }
  /* Back */
  .card-back {
    left: 621px;
    width: 515px;
    background: var(--back-blue);
  }
  .back-watermark-name {
    position: absolute;
    left: 17px; top: 244px;
    font-size: 38px;
    font-weight: 700;
    color: var(--faint);
    letter-spacing: -0.5px;
    white-space: nowrap;
  }
  .back-brand {
    position: absolute;
    right: 32px; top: 232px;
    text-align: center;
  }
  .back-brand .brand-name {
    font-size: 16px;
    font-weight: 700;
  }
  .back-brand .web {
    font-size: 12px;
    margin-top: 6px;
  }
</style>
</head>
<body>

<section class="card card-front" aria-label="Business card front">
  <header class="front-header">
    <h1 class="holder-name">MARCUS HALE</h1>
    <p class="holder-title">MANAGING DIRECTOR</p>
  </header>

  <div class="brand-circle">
    <span class="brand-name">LodgeBridgely</span>
  </div>

  <p class="address">48 Harbor Crest Avenue, #115<br>Fairmont, CA 90210</p>

  <ul class="contact-list">
    <li>
      <svg class="contact-icon" viewBox="0 0 16 16" aria-hidden="true">
        <circle cx="8" cy="8" r="7.2" fill="none" stroke="#fff" stroke-width="1.2"/>
        <path d="M5.4 4.3l1.3 1.6-.7.9c.5 1 1.3 1.9 2.4 2.5l.9-.7 1.6 1.3-.8 1.3c-2.6-.5-4.6-2.6-5.1-5.2z" fill="#fff"/>
      </svg>
      555.210.4837
    </li>
    <li>
      <svg class="contact-icon" viewBox="0 0 16 16" aria-hidden="true">
        <circle cx="8" cy="8" r="7.2" fill="none" stroke="#fff" stroke-width="1.2"/>
        <path d="M5.4 4.3l1.3 1.6-.7.9c.5 1 1.3 1.9 2.4 2.5l.9-.7 1.6 1.3-.8 1.3c-2.6-.5-4.6-2.6-5.1-5.2z" fill="#fff"/>
      </svg>
      555.367.9024
    </li>
    <li>
      <svg class="contact-icon" viewBox="0 0 16 16" aria-hidden="true">
        <circle cx="8" cy="8" r="8" fill="#fff"/>
        <rect x="4.3" y="5.3" width="7.4" height="5.4" rx="0.6" fill="#2f8fd2"/>
        <path d="M4.6 5.6L8 8.3l3.4-2.7" fill="none" stroke="#fff" stroke-width="0.9"/>
      </svg>
      info@lodgebridgely.net
    </li>
    <li>
      <svg class="contact-icon" viewBox="0 0 16 16" aria-hidden="true">
        <circle cx="8" cy="8" r="7.2" fill="none" stroke="#fff" stroke-width="1.2"/>
        <ellipse cx="8" cy="8" rx="2.8" ry="7" fill="none" stroke="#fff" stroke-width="1"/>
        <path d="M1 8h14M2 4.8h12M2 11.2h12" stroke="#fff" stroke-width="1"/>
      </svg>
      www.lodgebridgely.net
    </li>
  </ul>
</section>

<section class="card card-back" aria-label="Business card back">
  <span class="back-watermark-name" aria-hidden="true">LodgeBridgely</span>
  <div class="back-brand">
    <p class="brand-name">LodgeBridgely</p>
    <p class="web">www.lodgebridgely.net</p>
  </div>
</section>

</body>
</html>
```